175th Anniversary of Family Owned Funeral Home Pole Banners

We are family owned and operated funeral home in the Greater Cincinnati area and operate 3 funeral homes and a cremation center and we will be celebrating our 175th anniversary in 2015. The communities we serve look to us as leaders in the community and we are very well recognized. In preparation for next year, part of our planning includes placing pole banners in our local communities and our funeral home parking areas. The banner dimensions will be 30 x 60. We need for the banners to display a great message of tradition and excellence. Our website is www.brackenholloway.com I have uploaded an example of a pole banner as well as our logo(s).
Updates
Original artwork has been uploaded if needed.
Industry/Entity Type
Funeral Home

```html
<!DOCTYPE html>
<html lang="en">
<head>
<meta charset="utf-8">
<title>175th Anniversary Pole Banner</title>
<link href="https://fonts.googleapis.com/css2?family=Lobster&family=Lora:wght@400;500&family=Stardos+Stencil:wght@700&display=swap" rel="stylesheet">
<style>
  :root {
    --navy: #0c1a33;
    --footer-bg: #f4f5f6;
    --footer-line: #b9bbbe;
    --mark-grey: #8e929c;
    --gold-start: #e8911f;
    --gold-end: #e6be1e;
    --gold-deep: #d38a22;
    --white: #ffffff;
    --brand-blue: #5b7d98;
    --pole: #888888;
    --page: #ffffff;
  }
  * { margin: 0; padding: 0; box-sizing: border-box; }
  html, body {
    width: 1200px; height: 1000px; overflow: hidden;
    background: var(--page);
  }
  .canvas { position: relative; width: 1200px; height: 1000px; }

  .banner {
    position: absolute;
    width: 426px; height: 850px;
    border: 1px solid var(--footer-line);
    background: var(--footer-bg);
    overflow: hidden;
  }
  .banner--large { left: 166px; top: 48px; }
  .banner--pole {
    left: 911px; top: 183px;
    transform: scale(0.3897);
    transform-origin: top left;
  }

  .banner__field {
    position: absolute; left: 0; top: 0;
    width: 100%; height: 700px;
    background: var(--navy);
  }
  .banner__emblem {
    position: absolute; left: 148px; top: 62px;
    width: 120px; height: 120px;
    border-radius: 50%;
    background: var(--mark-grey);
  }
  .banner__number {
    position: absolute; left: 96px; top: 268px;
    font-family: "Lobster", cursive;
    font-size: 128px; line-height: 1;
    transform: rotate(-8deg);
    background: linear-gradient(90deg, var(--gold-start), var(--gold-end));
    -webkit-background-clip: text; background-clip: text;
    color: transparent;
  }
  .banner__number sup {
    font-size: 46px; vertical-align: 66px; margin-left: 4px;
  }
  .banner__title {
    position: absolute; left: 44px; top: 392px;
    font-family: "Lobster", cursive;
    font-size: 68px; line-height: 1;
    transform: rotate(-10deg);
    background: linear-gradient(90deg, var(--gold-start), var(--gold-end) 70%, var(--gold-deep));
    -webkit-background-clip: text; background-clip: text;
    color: transparent;
  }
  .banner__tagline {
    position: absolute; left: 0; top: 506px; width: 100%;
    font-family: "Stardos Stencil", serif;
    font-weight: 700;
    font-size: 29px; letter-spacing: 2px;
    color: var(--white);
    list-style: none;
  }
  .banner__tagline li { position: absolute; white-space: nowrap; }
  .banner__tagline li:nth-child(1) { left: 138px; top: 0; }
  .banner__tagline li:nth-child(2) { left: 134px; top: 45px; }
  .banner__tagline li:nth-child(3) { left: 104px; top: 90px; }

  .banner__footer {
    position: absolute; left: 0; top: 700px;
    width: 100%; height: 150px;
    font-family: "Lora", serif;
    color: var(--brand-blue);
  }
  .brand__square {
    position: absolute; left: 64px; top: 44px;
    width: 30px; height: 30px;
    background: var(--brand-blue);
  }
  .brand__name {
    position: absolute; left: 108px; top: 38px;
    font-size: 32px; font-weight: 400; line-height: 1;
  }
  .brand__descriptor {
    position: absolute; left: 64px; top: 88px;
    font-size: 15px; line-height: 1;
  }

  .pole {
    position: absolute; left: 880px; top: 148px;
    width: 9px; height: 605px;
    background: var(--pole);
  }
  .pole__arm {
    position: absolute; left: 889px;
    width: 22px; height: 5px;
    background: var(--pole);
  }
  .pole__arm--top { top: 233px; }
  .pole__arm--bottom { top: 443px; }
</style>
</head>
<body>
<main class="canvas">

  <section class="banner banner--large">
    <div class="banner__field">
      <div class="banner__emblem"></div>
      <div class="banner__number">175<sup>th</sup></div>
      <div class="banner__title">Anniversary</div>
      <ul class="banner__tagline">
        <li>TRADITION,</li>
        <li>EXCELLENCE</li>
        <li>AND COMPASSION</li>
      </ul>
    </div>
    <footer class="banner__footer">
      <span class="brand__square"></span>
      <span class="brand__name">Bracken Holloway</span>
      <span class="brand__descriptor">Family Funeral Homes &amp; Cremation Center</span>
    </footer>
  </section>

  <div class="pole"></div>
  <div class="pole__arm pole__arm--top"></div>
  <div class="pole__arm pole__arm--bottom"></div>

  <section class="banner banner--pole" aria-hidden="true">
    <div class="banner__field">
      <div class="banner__emblem"></div>
      <div class="banner__number">175<sup>th</sup></div>
      <div class="banner__title">Anniversary</div>
      <ul class="banner__tagline">
        <li>TRADITION,</li>
        <li>EXCELLENCE</li>
        <li>AND COMPASSION</li>
      </ul>
    </div>
    <footer class="banner__footer">
      <span class="brand__square"></span>
      <span class="brand__name">Bracken Holloway</span>
      <span class="brand__descriptor">Family Funeral Homes &amp; Cremation Center</span>
    </footer>
  </section>

</main>
</body>
</html>
```